New Business Aquisition Postcard Project

Create a post card for new client acquisition. The postcard is to promote our new campaign, our SAVE YOU OR SEND YOU MONEY Campaign. We have preselected people that we know we are highly likely to save money. These people own homes, valued 100k or over, these homes were built after the year 2000 and are within a radius of our office. If we cannot save them $307 (the average savings experienced by our customers) a year on their home and auto insurance combined, we will send them a $20 gift card for wasting their time.

Target Market(s)

This mailing will be sent to confirmed homeowners in Western Pennsylvania. These people own a home built after the year 2000.

Industry/Entity Type

Car Insurance

Font styles to use
Serif

Colors
0355a3

Requirements
Must have
• I have included a picture of the flyer I created. We need to include testimonials. I have those on the flyer and more.
Nice to have
• This should be laid out and ready to go in a postcard format. I have not decided if I will use labels or just run the postcards through my printer to put the names on. Where the flyer uses a person's name, the postcard should use "Pennsylvania Homeowner". It could also say "Attention to Pennsylvania Homeowners with homes built after the year 2000." Remember, we have preselected this people and we can let them know that. This offer will only be going to highly qualified prospects and will not be plastered all over town, so to speak.

```html
<!DOCTYPE html>
<html lang="en">
<head>
<meta charset="utf-8">
<title>Daniel Hale Agency – Save You or Send You Money Postcard</title>
<link rel="stylesheet" href="https://fonts.googleapis.com/css2?family=Open+Sans:ital,wght@0,400;0,600;0,700;1,600&family=Oswald:wght@500;600&family=Roboto+Slab:wght@800&family=Architects+Daughter&display=swap">
<style>
  :root {
    --brand-blue: #0355a3;
    --bright-blue: #1b7fd1;
    --sky-blue: #2a74c9;
    --ink: #2b2b2b;
    --grey: #6b6b6b;
    --light-grey: #b9b9b9;
    --paper: #ffffff;
    --line: #c8c8c8;
  }
  * { box-sizing: border-box; margin: 0; padding: 0; }
  html, body {
    width: 933px; height: 1200px; overflow: hidden;
    background: var(--paper);
    font-family: "Open Sans", Arial, sans-serif;
    color: var(--ink);
  }
  .postcard {
    position: absolute; left: 31px; width: 839px; height: 545px;
    background: var(--paper); overflow: hidden;
    border: 1px solid #e2e2e2;
  }
  .postcard--front { top: 30px; height: 541px; }
  .postcard--back { top: 590px; }
  .layer { position: absolute; }

  /* front */
  .sky-backdrop {
    left: 0; top: 0; width: 839px; height: 300px;
    background: linear-gradient(180deg, #2f6fc4 0%, #6fa6e0 45%, #c9def2 62%, #7fb54a 80%, #4f8f2a 100%);
  }
  .front-swoosh { left: 0; top: 0; width: 839px; height: 541px; }
  .family-photo {
    left: 55px; top: 95px; width: 360px; height: 275px;
    border-radius: 40% 40% 6px 6px / 30% 30% 6px 6px;
    background: radial-gradient(ellipse at 50% 45%, #e9c6a8 0%, #c89a78 35%, #8a6a55 60%, #3d5f8f 85%, rgba(61,95,143,0.2) 100%);
  }
  .home-photo {
    left: 470px; top: 35px; width: 365px; height: 310px;
    border-radius: 6px;
    background: linear-gradient(180deg, #d2c7b2 0%, #b7ab92 40%, #e8e6e0 62%, #8c8f94 78%, #c8323a 90%, #7fb54a 100%);
  }
  .quote-mark {
    left: 53px; top: -6px;
    font-family: Georgia, serif; font-size: 110px; line-height: 1;
    color: #e6e6e6; font-weight: 700;
  }
  .quote-rule { left: 142px; top: 22px; width: 2px; height: 70px; background: #ffffff; }
  .testimonial {
    left: 151px; top: 24px; width: 285px;
    font-style: italic; font-weight: 600; font-size: 11.5px; line-height: 14px;
    color: #ffffff;
  }
  .call-now {
    left: 420px; top: 284px;
    font-family: "Open Sans", sans-serif; font-weight: 700; font-size: 36px; line-height: 34px;
    color: var(--bright-blue); transform: rotate(-8deg);
  }
  .free-quote {
    left: 442px; top: 364px;
    font-family: "Roboto Slab", Georgia, serif; font-weight: 800; font-size: 14px;
    color: var(--ink); letter-spacing: 0.3px;
  }
  .attention {
    left: 50px; top: 376px; width: 400px; text-align: center;
    font-family: "Oswald", "Arial Narrow", sans-serif; font-weight: 500;
    font-size: 19px; line-height: 27px; color: var(--ink);
    transform: scaleY(1.08); transform-origin: top;
  }
  .attention strong { color: var(--brand-blue); font-size: 25px; font-weight: 600; }
  .guarantee {
    left: 30px; top: 468px; width: 440px;
    font-family: "Architects Daughter", cursive; font-size: 17px; line-height: 27px;
    color: var(--brand-blue);
  }
  .agency-name {
    left: 478px; top: 378px; width: 345px; text-align: right;
    font-family: "Open Sans", sans-serif; font-weight: 400;
    font-size: 37px; line-height: 44px; color: var(--brand-blue); letter-spacing: 0.5px;
  }
  .agency-tag {
    font-size: 20px; letter-spacing: 1px;
  }
  .front-phone {
    left: 478px; top: 450px; width: 345px; text-align: center;
    font-weight: 600; font-size: 29px; color: var(--grey);
  }
  .front-web {
    left: 478px; top: 494px; width: 345px; text-align: center;
    font-weight: 700; font-size: 17.5px; color: var(--grey); letter-spacing: 0.5px;
  }

  /* back */
  .back-swoosh { left: 0; top: 0; width: 839px; height: 545px; }
  .back-agency {
    left: 48px; top: 32px;
    font-weight: 400; font-size: 34px; line-height: 40px; color: var(--brand-blue); letter-spacing: 0.5px;
  }
  .back-agency .agency-tag { font-size: 18px; }
  .letter {
    left: 26px; top: 118px; width: 380px;
    font-size: 12px; line-height: 17.5px; color: var(--ink); letter-spacing: -0.2px;
  }
  .letter p { margin-bottom: 7px; }
  .letter .cta { font-weight: 700; }
  .signature {
    left: 219px; top: 348px;
    font-family: "Architects Daughter", cursive; font-size: 17px; color: var(--brand-blue);
  }
  .home-car-art {
    left: 28px; top: 380px; width: 150px; height: 112px; border-radius: 10px;
    background: radial-gradient(ellipse at 55% 45%, #6fa7e6 0%, #2f74c9 45%, #e9f0f8 75%, rgba(255,255,255,0) 100%);
  }
  .quotes-box {
    left: 184px; top: 388px; width: 218px; height: 94px;
    border: 2px solid #6fa2d8; border-radius: 6px; padding: 4px 0 0 28px;
  }
  .quotes-box h2 {
    font-size: 19px; font-weight: 700; color: var(--brand-blue); line-height: 22px;
  }
  .quotes-box h2 span { color: var(--grey); font-weight: 600; }
  .quotes-box ul { list-style: none; }
  .quotes-box li {
    font-size: 15px; font-weight: 700; line-height: 19px; color: var(--bright-blue);
    display: flex; align-items: center; gap: 10px;
  }
  .quotes-box li:nth-child(2) { color: var(--grey); }
  .quotes-box svg { width: 11px; height: 11px; }
  .return-address {
    left: 441px; top: 30px;
    font-size: 12.5px; line-height: 16.5px; color: var(--ink);
  }
  .stamp-box {
    left: 711px; top: 26px; width: 98px; height: 107px;
    border: 1px dashed #bdbdbd;
  }
  .mail-line {
    left: 468px; width: 318px; height: 0;
    border-top: 1px dashed #bdbdbd;
  }
</style>
</head>
<body>

<section class="postcard postcard--front">
  <div class="layer sky-backdrop" role="img" aria-label="Blue sky with clouds over a green lawn"></div>
  <svg class="layer front-swoosh" viewBox="0 0 839 541" aria-hidden="true">
    <path d="M0 272 Q300 250 560 300 Q720 325 839 255 L839 541 L0 541 Z" fill="#1f64b8"/>
    <path d="M0 288 Q300 262 560 312 Q720 340 839 266 L839 541 L0 541 Z" fill="#ffffff"/>
  </svg>
  <div class="layer home-photo" role="img" aria-label="Two-storey family home with a garage and two cars parked in front"></div>
  <div class="layer family-photo" role="img" aria-label="Smiling family of four sitting with their golden retriever"></div>

  <div class="layer quote-mark">&ldquo;</div>
  <div class="layer quote-rule"></div>
  <p class="layer testimonial">&ldquo;Daniel helped us SAVE $642 per year on our auto and home insurance. He simplified our three policies, got us a new low monthly payment, all while increasing our coverages.&rdquo;</p>

  <div class="layer call-now">Call<br>NOW</div>
  <div class="layer free-quote">FOR A FREE QUOTE!</div>

  <h1 class="layer attention"><strong>ATTENTION!</strong> NEW LOWERED RATES FOR<br>PENNSYLVANIA HOMEOWNERS WITH HOMES<br>BUILT AFTER THE YEAR 2000:</h1>

  <p class="layer guarantee">&ldquo;If I can&rsquo;t save you at least $307.00 per year on<br>your Auto and Home Insurance, I&rsquo;ll pay you $20!&rdquo;</p>

  <div class="layer agency-name">DANIEL HALE <span class="agency-tag">AGENCY</span></div>
  <div class="layer front-phone">(724) 555-0148</div>
  <div class="layer front-web">WWW.QUOTEMEDANIEL.COM</div>
</section>

<section class="postcard postcard--back">
  <svg class="layer back-swoosh" viewBox="0 0 839 545" aria-hidden="true">
    <path d="M392 0 Q440 40 430 300 Q426 450 400 535 Q445 420 448 280 Q452 80 420 0 Z" fill="#1f64b8"/>
    <path d="M402 0 Q445 40 438 300 Q434 430 418 500 Q440 410 444 280 Q448 90 415 0 Z" fill="#8cc0ee"/>
  </svg>

  <div class="layer back-agency">DANIEL HALE <span class="agency-tag">AGENCY</span></div>

  <div class="layer letter">
    <p>Dear Homeowner,</p>
    <p>The auto &amp; home insurance carriers I work with just LOWERED RATES in Pennsylvania! We&rsquo;ve been helping your neighbors save hundreds of dollars per year.</p>
    <p>In fact, I&rsquo;m so confident I can save you money&hellip; If I can&rsquo;t save you at least $307.00 - I&rsquo;ll pay you $20 as my penalty just for wasting your time. (You just need to qualify for auto and home insurance.)</p>
    <p>ONE CALL DOES IT ALL! We&rsquo;ll cancel your existing policies for you, request any refund you may be owed, PLUS notify DMV, your bank, and contact your mortgage company for escrow payment, so the process is easy and pain-free for you!!</p>
    <p class="cta">Call (724) 555-0148 or visit QUOTEMEDANIEL.COM!</p>
  </div>
  <div class="layer signature">Daniel Hale</div>

  <div class="layer home-car-art" role="img" aria-label="Small blue house with a blue car in front"></div>
  <div class="layer quotes-box">
    <h2>OUR <span>QUOTES</span></h2>
    <ul>
      <li><svg viewBox="0 0 12 12"><path d="M1 6 L4.5 10 L11 1" fill="none" stroke="currentColor" stroke-width="1.8"/></svg>Fast</li>
      <li><svg viewBox="0 0 12 12"><path d="M1 6 L4.5 10 L11 1" fill="none" stroke="currentColor" stroke-width="1.8"/></svg>Free</li>
      <li><svg viewBox="0 0 12 12"><path d="M1 6 L4.5 10 L11 1" fill="none" stroke="currentColor" stroke-width="1.8"/></svg>Easy</li>
    </ul>
  </div>

  <address class="layer return-address" style="font-style:normal">
    418 Linden Avenue<br>Greensburg, PA 15601<br>(724) 555-0148<br>QUOTEMEDANIEL.COM
  </address>
  <div class="layer stamp-box"></div>
  <div class="layer mail-line" style="top:262px"></div>
  <div class="layer mail-line" style="top:320px"></div>
  <div class="layer mail-line" style="top:378px"></div>
</section>

</body>
</html>
```